Letterbox flyer design

Hi - hoping you're able to help design a flyer for letterbox delivery. I think it needs to be 99mm x 210mm.

Side 1 - Large Logo, dark back ground.
Larger text - "5%* Property Management."
Medium Text - "Better Services, Lower Fee's, Higher Yields"
Smaller text at bottom - "0427 519 684 - marcus@kelbridge.com.au - kelbridge.com.au"

Back Side -
• Management Fee – 5%+GST of rent collected (no rent paid = no mgmt. fee charged)
• An Establishment fee of $500 for new tenancies we establish.
• Marketing Costs as Required and agreed to between parties.
• No Fee’s for Condition Reports, inspections, re-listing, tenancy renewal, admin costs, or any other ‘sundry’ charges.
• All rent is paid out monthly, yearly ‘profit-and-loss’ statements at no cost.
• Ingoing condition report is produced prior to occupancy, and routine condition inspections are conducted after the first 3months, then every 6months.
• Open homes are advertised in advance, and held on the weekend and one lunchtime or evening per week.
• All applicants are vetted, with the most suitable sent through for your consideration and approval.
• Advise on different tenancy terms as they could have the ability to affect the long-term yields.

```html
<!DOCTYPE html>
<html lang="en">
<head>
<meta charset="utf-8">
<title>Kelbridge &amp; Co Property Services – Letterbox Flyer</title>
<link rel="stylesheet" href="https://fonts.googleapis.com/css2?family=Anton&family=Bebas+Neue&family=Lato:wght@400;700;900&display=swap">
<style>
  :root {
    --stage: #d9d9d9;
    --black: #000000;
    --navy: #1c3549;
    --teal: #43bfc9;
    --grey-light: #c4c4c6;
    --grey-dark: #5e5a5e;
    --brand-grey: #8a8a8d;
    --white: #ffffff;
  }
  * { margin: 0; padding: 0; box-sizing: border-box; }
  html, body {
    width: 1077px;
    height: 1200px;
    overflow: hidden;
    background: var(--stage);
  }
  .flyer {
    position: absolute;
    top: 219.5px;
    width: 359px;
    height: 761px;
    box-shadow: 0 1px 3px rgba(0,0,0,0.25);
    overflow: hidden;
  }
  .flyer--front { left: 151px; background: var(--black); }
  .flyer--back  { left: 567.5px; background: var(--navy); }

  .front-art { position: absolute; inset: 0; width: 359px; height: 761px; }
  .brand-name { font-family: "Lato", sans-serif; font-weight: 700; }
  .tagline { font-family: "Bebas Neue", "Oswald", sans-serif; }
  .headline { font-family: "Anton", "Oswald", sans-serif; }

  .contact {
    position: absolute;
    left: 0; right: 0;
    top: 675px;
    text-align: center;
    color: var(--white);
    font-family: "Lato", sans-serif;
  }
  .contact__line {
    display: flex;
    align-items: center;
    justify-content: center;
    gap: 5px;
    line-height: 23px;
    font-size: 18px;
    font-weight: 400;
  }
  .contact__line--phone { font-size: 19.5px; font-weight: 700; }
  .contact__icon { width: 14px; height: 14px; flex: none; }

  .back-frame {
    position: absolute;
    left: 15.4px; top: 16.6px;
    width: 328.4px; height: 730.2px;
    border: 2px solid var(--teal);
  }
  .features {
    position: absolute;
    left: 42px; top: 39px;
    width: 283px;
    list-style: none;
    font-family: "Lato", sans-serif;
    font-weight: 700;
    font-size: 15px;
    line-height: 18.6px;
    color: var(--white);
    hyphens: manual;
  }
  .features__item {
    display: flex;
    gap: 9px;
    margin-bottom: 18.3px;
  }
  .features__text { width: 258px; }
  .features__tick { width: 16px; height: 16px; flex: none; margin-top: 1px; }
</style>
</head>
<body>

<section class="flyer flyer--front" aria-label="Flyer front">
  <svg class="front-art" viewBox="0 0 359 761" xmlns="http://www.w3.org/2000/svg">
    <!-- bands -->
    <polygon points="0,174 359,122.5 359,124.5 0,183" fill="var(--grey-light)"/>
    <polygon points="0,183 359,124.5 359,126.5 0,194.7" fill="var(--grey-dark)"/>
    <polygon points="0,194.7 359,126.5 359,602 0,673" fill="var(--navy)"/>
    <polygon points="359,602 359,612 0,673" fill="var(--grey-dark)"/>
    <polygon points="359,612 359,621.5 0,673" fill="var(--grey-light)"/>

    <!-- brand -->
    <text class="brand-name" x="179.5" y="70" font-size="30" text-anchor="middle" fill="var(--brand-grey)">Kelbridge &amp; Co</text>
    <text class="brand-name" x="179.5" y="98" font-size="19" text-anchor="middle" fill="var(--brand-grey)">Property Services</text>

    <!-- headline -->
    <text class="headline" x="62" y="354.5" font-size="180" textLength="228" lengthAdjust="spacingAndGlyphs" fill="var(--teal)">5%</text>
    <text class="headline" x="276" y="296" font-size="110" fill="var(--teal)">*</text>
    <text class="headline" x="38.5" y="424" font-size="58" textLength="280" lengthAdjust="spacingAndGlyphs" fill="var(--teal)">PROPERTY</text>
    <text class="headline" x="38.5" y="477" font-size="48" textLength="281" lengthAdjust="spacingAndGlyphs" fill="var(--teal)">MANAGEMENT.</text>

    <!-- taglines -->
    <text class="tagline" x="84.6" y="524" font-size="34" textLength="183" lengthAdjust="spacingAndGlyphs" fill="var(--white)">BETTER SERVICES</text>
    <text class="tagline" x="109" y="563" font-size="34" textLength="133" lengthAdjust="spacingAndGlyphs" fill="var(--white)">LOWER FEE'S</text>
    <text class="tagline" x="99" y="603" font-size="34" textLength="155" lengthAdjust="spacingAndGlyphs" fill="var(--white)">HIGHER YIELDS</text>
  </svg>

  <div class="contact">
    <p class="contact__line contact__line--phone">
      <svg class="contact__icon" viewBox="0 0 24 24" aria-hidden="true"><path fill="var(--teal)" d="M6.6 10.8c1.4 2.8 3.8 5.1 6.6 6.6l2.2-2.2c.3-.3.7-.4 1-.2 1.1.4 2.3.6 3.6.6.6 0 1 .4 1 1V20c0 .6-.4 1-1 1C10.6 21 3 13.4 3 4c0-.6.4-1 1-1h3.5c.6 0 1 .4 1 1 0 1.3.2 2.5.6 3.6.1.3 0 .7-.2 1z"/></svg>
      0427 519 684
    </p>
    <p class="contact__line">
      <svg class="contact__icon" viewBox="0 0 24 24" aria-hidden="true"><rect x="2" y="5" width="20" height="14" fill="var(--teal)"/><path d="M2 5l10 8 10-8" fill="none" stroke="var(--black)" stroke-width="1.6"/></svg>
      marcus@kelbridge.com.au
    </p>
    <p class="contact__line">
      <svg class="contact__icon" viewBox="0 0 24 24" aria-hidden="true"><circle cx="12" cy="12" r="10" fill="var(--teal)"/><path d="M2 12h20M12 2c3 3 3 17 0 20M12 2c-3 3-3 17 0 20" fill="none" stroke="var(--black)" stroke-width="1.3"/></svg>
      kelbridge.com.au
    </p>
  </div>
</section>

<section class="flyer flyer--back" aria-label="Flyer back">
  <div class="back-frame"></div>
  <ul class="features">
    <li class="features__item"><svg class="features__tick" viewBox="0 0 16 16" aria-hidden="true"><circle cx="8" cy="8" r="8" fill="var(--teal)"/><path d="M4.3 8.2l2.5 2.5 5-5" fill="none" stroke="var(--navy)" stroke-width="2"/></svg><span class="features__text">Management Fee – 5%+GST of rent collected (no rent paid = no mgmt. fee charged)</span></li>
    <li class="features__item"><svg class="features__tick" viewBox="0 0 16 16" aria-hidden="true"><circle cx="8" cy="8" r="8" fill="var(--teal)"/><path d="M4.3 8.2l2.5 2.5 5-5" fill="none" stroke="var(--navy)" stroke-width="2"/></svg><span class="features__text">An Establishment fee of $500 for new tenancies we establish.</span></li>
    <li class="features__item"><svg class="features__tick" viewBox="0 0 16 16" aria-hidden="true"><circle cx="8" cy="8" r="8" fill="var(--teal)"/><path d="M4.3 8.2l2.5 2.5 5-5" fill="none" stroke="var(--navy)" stroke-width="2"/></svg><span class="features__text">Marketing Costs as Required and agreed to between parties.</span></li>
    <li class="features__item"><svg class="features__tick" viewBox="0 0 16 16" aria-hidden="true"><circle cx="8" cy="8" r="8" fill="var(--teal)"/><path d="M4.3 8.2l2.5 2.5 5-5" fill="none" stroke="var(--navy)" stroke-width="2"/></svg><span class="features__text">No Fee’s for Condition Reports, in&shy;spections, re-listing, tenancy re&shy;newal, admin costs, or any other ‘sundry’ charges.</span></li>
    <li class="features__item"><svg class="features__tick" viewBox="0 0 16 16" aria-hidden="true"><circle cx="8" cy="8" r="8" fill="var(--teal)"/><path d="M4.3 8.2l2.5 2.5 5-5" fill="none" stroke="var(--navy)" stroke-width="2"/></svg><span class="features__text">All rent is paid out monthly, yearly ‘profit-and-loss’ statements at no cost.</span></li>
    <li class="features__item"><svg class="features__tick" viewBox="0 0 16 16" aria-hidden="true"><circle cx="8" cy="8" r="8" fill="var(--teal)"/><path d="M4.3 8.2l2.5 2.5 5-5" fill="none" stroke="var(--navy)" stroke-width="2"/></svg><span class="features__text">Ingoing condition report is pro&shy;duced prior to occupancy, and rou&shy;tine condition inspections are con&shy;ducted after the first 3months, then every 6months.</span></li>
    <li class="features__item"><svg class="features__tick" viewBox="0 0 16 16" aria-hidden="true"><circle cx="8" cy="8" r="8" fill="var(--teal)"/><path d="M4.3 8.2l2.5 2.5 5-5" fill="none" stroke="var(--navy)" stroke-width="2"/></svg><span class="features__text">Open homes are advertised in ad&shy;vance, and held on the weekend and one lunchtime or evening per week.</span></li>
    <li class="features__item"><svg class="features__tick" viewBox="0 0 16 16" aria-hidden="true"><circle cx="8" cy="8" r="8" fill="var(--teal)"/><path d="M4.3 8.2l2.5 2.5 5-5" fill="none" stroke="var(--navy)" stroke-width="2"/></svg><span class="features__text">All applicants are vetted, with the most suitable sent through for your consideration and approval.</span></li>
    <li class="features__item"><svg class="features__tick" viewBox="0 0 16 16" aria-hidden="true"><circle cx="8" cy="8" r="8" fill="var(--teal)"/><path d="M4.3 8.2l2.5 2.5 5-5" fill="none" stroke="var(--navy)" stroke-width="2"/></svg><span class="features__text">Advise on different tenancy terms as they could have the ability to affect the long-term yields.</span></li>
  </ul>
</section>

</body>
</html>
```